Newsletter-Design für eine Yogalehrerin
Zielgruppe
Ich bin Yogalehrerin.
Meine Zielgruppe sind hauptsächlich Erwachsene (Frauen und Männer) welche Privatyoga Online praktizieren.
Aufgabenstellung
Gerne auch, aber nicht nur das Layout und die Texte von der Webseite www.atemkreis-nord.ch verwenden.
Es sollte ein ansprechender Newsletter für Online Privatyoga gestaltet werden um mehr Teilnehmer zu gewinnen.

```html
<!DOCTYPE html>
<html lang="de">
<head>
<meta charset="utf-8">
<title>Atemkreis Nord – Newsletter Online Yoga</title>
<link href="https://fonts.googleapis.com/css2?family=Roboto:wght@300;400;500;700&display=swap" rel="stylesheet">
<style>
:root{
  --page:#efeeec;
  --card:#ffffff;
  --ink:#1f1f1f;
  --text:#333333;
  --accent:#ee6a3c;
  --button:#e9522b;
  --line:#ececec;
  --adults:#9b88c9;
  --kids:#f2968a;
  --pregnant:#7cc7e2;
  --seniors:#5db4a6;
  --private:#f6db78;
}
*{box-sizing:border-box;margin:0;padding:0}
html,body{width:863px;height:1200px;overflow:hidden;background:var(--page)}
body{font-family:"Roboto",Arial,sans-serif;color:var(--text)}
.stage{width:1308px;height:1818px;transform:scale(.66);transform-origin:0 0;position:relative;background:var(--page)}
.newsletter{position:absolute;left:271px;top:40px;width:765px;height:1602px;background:var(--card)}
.brand{position:absolute;top:15px;left:0;width:100%;text-align:center}
.brand-mark{width:62px;height:62px;border-radius:50%;border:2px solid var(--accent);margin:0 auto}
.brand-name{margin-top:8px;font-size:30px;font-weight:400;letter-spacing:2px;color:var(--accent);text-transform:uppercase}
.courses{position:absolute;top:145px;left:30px;width:705px;height:355px;display:flex}
.course{flex:1;display:flex;flex-direction:column}
.course-photo{height:257px}
.course-label{flex:1;color:#fff;font-size:12px;line-height:14px;padding:35px 0 0 30px}
.c-adults .course-photo{background:linear-gradient(160deg,#d9c2ae,#7a4a3a)}
.c-kids .course-photo{background:linear-gradient(160deg,#eeeef2,#c9c4d6)}
.c-pregnant .course-photo{background:linear-gradient(160deg,#f4ece6,#e2c3ae)}
.c-seniors .course-photo{background:linear-gradient(160deg,#9fb7c4,#3d6a86)}
.c-private .course-photo{background:linear-gradient(160deg,#eeeef2,#e4c8b8)}
.c-adults .course-label{background:var(--adults)}
.c-kids .course-label{background:var(--kids)}
.c-pregnant .course-label{background:var(--pregnant)}
.c-seniors .course-label{background:var(--seniors)}
.c-private .course-label{background:var(--private)}
.section-title{position:absolute;left:30px;font-size:26px;font-weight:400;color:var(--accent)}
.benefits{position:absolute;left:30px;top:595px;width:690px;font-size:11.5px;line-height:17px;color:var(--ink)}
.benefits p{margin-bottom:17px}
.benefits strong{font-weight:700}
.voucher{position:absolute;left:30px;top:778px;width:706px;height:254px;border:1px solid var(--line);display:flex}
.voucher-photo{width:352px;height:100%;background:linear-gradient(135deg,#e4d6c8 0%,#f2b58a 45%,#efe3d4 75%,#d9c9b8 100%)}
.voucher-info{padding:50px 0 0 30px}
.voucher-title{font-size:26px;line-height:31px;font-weight:400;color:var(--ink)}
.voucher-price{margin-top:17px;font-size:20px;font-weight:300;color:var(--accent)}
.btn{display:inline-block;background:var(--button);color:#fff;font-size:11px;font-weight:700;letter-spacing:.3px;text-transform:uppercase;border-radius:3px;text-align:center}
.voucher .btn{margin-top:24px;width:102px;height:37px;line-height:37px}
.steps{position:absolute;left:35px;top:1131px;width:700px;display:grid;grid-template-columns:358px 1fr;row-gap:17px;font-size:11.5px;line-height:17px;color:var(--ink);list-style:none}
.steps li{position:relative;padding-left:18px}
.steps li::before{content:"";position:absolute;left:1px;top:6px;width:5px;height:5px;border-radius:50%;background:var(--button)}
.path{position:absolute;left:30px;top:1317px;width:706px;height:233px}
.path-photo{position:absolute;inset:0;background:linear-gradient(180deg,#f6e4dc 0%,#f1d2c7 55%,#f6dcd2 100%)}
.path-box{position:absolute;left:62px;top:103px;width:581px;height:87px;background:#fff;display:flex;align-items:center;padding-left:30px}
.path-text{font-size:26px;font-weight:400;color:var(--ink)}
.path-box .btn{margin-left:24px;width:120px;height:37px;line-height:37px}
.footer{position:absolute;left:271px;top:1642px;width:765px;text-align:center}
.social{display:flex;justify-content:center;gap:8px;margin-top:18px}
.social span{width:34px;height:34px;border-radius:50%;background:#fff}
.unsubscribe{margin-top:22px;font-size:12px;color:var(--ink)}
</style>
</head>
<body>
<div class="stage">
  <main class="newsletter">
    <header class="brand">
      <div class="brand-mark"></div>
      <div class="brand-name">Atemkreis Nord</div>
    </header>

    <section class="courses">
      <div class="course c-adults"><div class="course-photo" role="img" aria-label="Mann meditiert mit gefalteten Händen"></div><div class="course-label">Yoga für<br>Erwachsene</div></div>
      <div class="course c-kids"><div class="course-photo" role="img" aria-label="Kind in Yogahaltung mit erhobenen Armen"></div><div class="course-label">Yoga für<br>Kinder</div></div>
      <div class="course c-pregnant"><div class="course-photo" role="img" aria-label="Bauch einer schwangeren Frau"></div><div class="course-label">Yoga für<br>Schwangere</div></div>
      <div class="course c-seniors"><div class="course-photo" role="img" aria-label="Ältere Frau meditiert am Fenster"></div><div class="course-label">Yoga für<br>Senioren</div></div>
      <div class="course c-private"><div class="course-photo" role="img" aria-label="Hand auf einer Schulter bei Privatstunde"></div><div class="course-label">Yoga<br>Privat</div></div>
    </section>

    <h2 class="section-title" style="top:548px">Welche Vorteile hat Online Yoga?</h2>
    <div class="benefits">
      <p><strong>Flexibel</strong> – mit Handy, Laptop oder PC, du kannst von jedem Ort aus Yoga praktizieren.</p>
      <p><strong>Kostengünstig</strong> – meine Kurse sind Online günstiger und du hast keine zusätzlichen Ausgaben (wie Verkehrsmittel etc.) um am Kurs teilzunehmen.</p>
      <p><strong>Zuverlässig</strong> – ich starte jeden Kurs ohne Teilnehmermindestanzahl.</p>
      <p><strong>Privatsphäre</strong> – du übst und entspannst dich in geschützter Atmosphäre.</p>
    </div>

    <section class="voucher">
      <div class="voucher-photo" role="img" aria-label="Geschenkgutschein-Karte mit Kerzen und Blüten"></div>
      <div class="voucher-info">
        <h3 class="voucher-title">Geschenkgutschein<br>Yoga Pakete</h3>
        <p class="voucher-price">29.00 CHF – 429.00 CHF</p>
        <span class="btn">Details</span>
      </div>
    </section>

    <h2 class="section-title" style="top:1083px">Wie funktioniert es?</h2>
    <ul class="steps">
      <li>Suche deinen Kurs / dein Yogazubehör aus</li>
      <li>Gib deine Kontaktdaten ein</li>
      <li>Lege deine Auswahl in den Warenkorb</li>
      <li>Folge dem Zahlungslink</li>
      <li>Gehe zur Kasse</li>
      <li>Schliesse deine Bestellung ab</li>
      <li>Falls du Yogazubehör bestellt hast, bekommst du es per Post zugesandt</li>
      <li>Du bekommst eine Bestätigungs-E-Mail und erhältst den Link zur Teilnahme an deinem Kurs</li>
    </ul>

    <section class="path">
      <div class="path-photo" role="img" aria-label="Gestapelte dunkle Steine vor rosafarbenem Hintergrund"></div>
      <div class="path-box">
        <p class="path-text">Der Weg des Yoga ist einzigartig.</p>
        <span class="btn">Alle Kurse</span>
      </div>
    </section>
  </main>

  <footer class="footer">
    <div class="social"><span></span><span></span></div>
    <p class="unsubscribe">Unsubscribe :-(</p>
  </footer>
</div>
</body>
</html>
```